Business Card Design and Stationary design for consulting firm

Harbourline Sourcing are looking for a new business card design and a design for their A4 letterhead / A4 invoices.

We are seeking to heavily increase our brand awareness and require a business card that's professional in appearance but also shows flare and innovation. A card design that people will remember.

About Us
Harbourline Sourcing are `The Sourcing Crew’.
Our mission is to be one of Australia’s greatest companies. Our aim is to help our customers achieve the best result from their purchasing experience.

Our Requirement:
• IMPACT! IMPACT! IMPACT!
• BUSINESS & PROFESSIONAL LOOKING

• Our business colours are orange, blue and green (See the logo attached).

We have provided an Art Design specification (attached) that needs to be followed for you to win the design. This also has the font, which is used on the logo.

We are after a two sided business card

Side One should have the:
The company Logo
The Sourcing Crew
www.harbourlinesourcing.com.au
Procure | Personnel | Probity & Privacy
Sydney | Melbourne | Adelaide | Brisbane

Side Two
Logo (optional)
Harbourline Sourcing (optional)
Employee details (details listed below)

The above format is our preferred option, but if you think you can come up with something better, feel free to put it forward.

We are leaving the design up to you, but it must incorporate the logo.

We will need a template that we can change the employee details on, as we will be adding more staff over the coming months.

The details below are for one employee per card with the same design.
------------------------

Employee Details:

Marcus Oldfield MBA, MMgmtStratProc
Principal Consultant
0412 356 917
Marcus@harbourlinesourcing.com.au

Brianna Tolhurst
Consulting Manager
0431 629 084
Brianna@harbourlinesourcing.com.au

Our website is www.harbourlinesourcing.com.au

The Letterhead / invoice needs to incorporate:
the company Logo
The Sourcing Crew
Sydney | Melbourne | Adelaide | Brisbane but otherwise the design is over to you.

This file needs to be delivered in word format as other detail will be added to the documents.

We look forward to you award winning designs. If you require any further information please feel free to contact us.

Regards
Harbourline Sourcing

Target Market(s)

Our Target market is companies with 80+ employees. The market we segment is heavily male based, between the ages of 35-55 years of age.

Industry/Entity Type

Consulting

Contact Information for Business Card

See Project Description

Font styles to use
Other font styles liked:
• See Art Specification

Requirements
Must have
• Company Colours, See Project Description
Should not have
• Be outside the Art specification guidelines

```html
<!DOCTYPE html>
<html lang="en">
<head>
<meta charset="utf-8">
<title>Harbourline Sourcing – Business Card</title>
<link rel="stylesheet" href="https://fonts.googleapis.com/css2?family=Open+Sans:wght@400;600;700&display=swap">
<style>
  :root {
    --bg: #e9e6e1;
    --blue: #1f82c8;
    --blue-deep: #0d5b9c;
    --blue-text: #1f7fc4;
    --orange: #f26a21;
    --ink: #3a3a3a;
    --white: #ffffff;
    --card-w: 720px;
    --card-h: 412px;
  }
  * { box-sizing: border-box; margin: 0; padding: 0; }
  html, body {
    width: 1200px; height: 950px; overflow: hidden;
    background: var(--bg);
    font-family: "Open Sans", Arial, sans-serif;
  }
  .canvas {
    width: 1200px; height: 950px;
    display: flex; flex-direction: column;
    align-items: center; justify-content: center; gap: 40px;
  }
  .card {
    position: relative;
    width: var(--card-w); height: var(--card-h);
    border-radius: 6px; overflow: hidden;
    box-shadow: 0 6px 18px rgba(0,0,0,0.18);
  }

  /* Side one */
  .card--back {
    background: linear-gradient(135deg, var(--blue) 0%, var(--blue-deep) 100%);
    color: var(--white);
    display: flex; flex-direction: column; align-items: center; justify-content: center;
    text-align: center;
  }
  .brand {
    display: flex; align-items: center; gap: 14px;
    font-weight: 700; letter-spacing: 0.5px;
  }
  .brand__dot { width: 22px; height: 22px; border-radius: 50%; }
  .card--back .brand { font-size: 40px; color: var(--white); margin-bottom: 34px; }
  .card--back .brand__dot { background: var(--white); width: 28px; height: 28px; }
  .tagline { font-size: 24px; font-weight: 700; margin-bottom: 6px; }
  .back-line { font-size: 19px; font-weight: 400; line-height: 1.45; opacity: 0.92; }

  /* Side two */
  .card--front { background: var(--white); }
  .accent-band {
    position: absolute; left: 0; right: 0; bottom: 0; height: 96px;
    background: linear-gradient(90deg, var(--blue) 0%, var(--blue-deep) 100%);
  }
  .card--front .brand {
    position: absolute; left: 40px; top: 120px;
    font-size: 25px; color: var(--ink); text-transform: uppercase; letter-spacing: 1px;
    flex-direction: column; align-items: flex-start; gap: 10px; line-height: 1.05;
  }
  .card--front .brand__dot { background: var(--blue); }
  .contact { position: absolute; left: 350px; top: 72px; color: var(--ink); }
  .contact__name { font-size: 27px; font-weight: 700; color: var(--blue-text); line-height: 1.15; }
  .contact__quals { font-size: 17px; font-weight: 600; color: var(--blue-text); }
  .contact__role { font-size: 18px; font-weight: 400; color: var(--orange); margin-bottom: 8px; }
  .contact__row {
    display: flex; align-items: center; gap: 10px;
    font-size: 17px; line-height: 1.55;
  }
  .contact__row svg { width: 16px; height: 16px; flex: none; fill: var(--blue-deep); }
</style>
</head>
<body>
<main class="canvas">

  <section class="card card--back" aria-label="Business card, side one">
    <div class="brand"><span class="brand__dot"></span>Harbourline Sourcing</div>
    <p class="tagline">The Sourcing Crew</p>
    <p class="back-line">www.harbourlinesourcing.com.au</p>
    <p class="back-line">Procure • Personnel • Probity &amp; Privacy</p>
    <p class="back-line">Sydney • Melbourne • Adelaide • Brisbane</p>
  </section>

  <section class="card card--front" aria-label="Business card, side two">
    <div class="accent-band" role="img" aria-label="Decorative sweeping band in blue with orange and green accents"></div>

    <div class="brand"><span class="brand__dot"></span>Harbourline<br>Sourcing</div>

    <div class="contact">
      <p class="contact__name">Marcus Oldfield</p>
      <p class="contact__quals">MBA, MMgmtStratProc</p>
      <p class="contact__role">Principal Consultant</p>
      <p class="contact__row">
        <svg viewBox="0 0 16 16"><path d="M3 1h3l1.5 4-2 1.3a9 9 0 0 0 4.2 4.2L11 8.5l4 1.5v3a2 2 0 0 1-2 2A13 13 0 0 1 1 3a2 2 0 0 1 2-2z"/></svg>
        0412 356 917
      </p>
      <p class="contact__row">
        <svg viewBox="0 0 16 16"><path d="M1 3h14v10H1z M1.5 3.5 8 9l6.5-5.5" stroke="#fff" stroke-width="1"/></svg>
        Marcus@harbourlinesourcing.com.au
      </p>
      <p class="contact__row">
        <svg viewBox="0 0 16 16"><circle cx="8" cy="8" r="7"/><path d="M1 8h14M8 1c3 3 3 11 0 14M8 1c-3 3-3 11 0 14" fill="none" stroke="#fff" stroke-width="1"/></svg>
        harbourlinesourcing.com.au
      </p>
    </div>
  </section>

</main>
</body>
</html>
```